CoverLantern.com website re-design - modern engaging website creation

We have an existing website. Www.CoverLantern.com - the content on the site and our widgets are custom built. But the layout and design of our site we just put there as we built the functionality around it. We want a new, bold, and modern design aimed at getting visitors to run a life insurance quote and ultimately apply. Our demographic is centered around those between the ages of 30-60. So we are looking at a complete site overhaul with better pictures, buttons, and an extremely modern design.

Target Market(s)

30-50 year olds

Industry/Entity Type

Life insurance

Coding

Coded - Design and coding required

Number of Pages Required

5+ page

Font styles to use
Other font styles liked:
• Rubik

Colors
0054AA
0677BA
7BADD7
CADEEF
E8F1F8
00AB8E
00BBA5
67D7C9
C6EFE9
E9F9F6
59FF00
82FF00
B8FF75
E3FFCB
F4FFEA

Requirements
Must have
• Matching color schemes from existing website. We have custom widgets on our site now and those must be . White space is important to make it simple for the user to navigate
Nice to have
• Same content - different more modern design
Should not have
• Colors outside of our current color scheme. Should NOT be too similar to our existing site.

```html
<!DOCTYPE html>
<html lang="en">
<head>
<meta charset="utf-8">
<title>CoverLantern – Life Insurance Online</title>
<link href="https://fonts.googleapis.com/css2?family=Montserrat:wght@300;400;700;800&family=Roboto:wght@400;500;700&display=swap" rel="stylesheet">
<style>
:root{
  --blue:#0054AA;
  --blue-dark:#0a4e9b;
  --green:#76bc21;
  --green-soft:#e3ffcb;
  --ink:#2d2f33;
  --text:#5d6168;
  --grey-band:#f1f3f6;
  --footer:#2b2d31;
  --white:#ffffff;
}
*{box-sizing:border-box;margin:0;padding:0}
html,body{width:1200px;height:4386px;overflow:hidden}
body{position:relative;background:var(--white);font-family:'Roboto',sans-serif;color:var(--text)}
.abs{position:absolute}

/* header */
.site-header{position:absolute;left:0;top:0;width:1200px;height:111px;background:var(--white);z-index:5}
.brand{position:absolute;left:110px;top:32px;font-family:'Montserrat',sans-serif;font-size:40px;font-weight:400;color:var(--blue);letter-spacing:-.5px}
.top-actions{position:absolute;top:16px;right:112px;display:flex;gap:12px}
.pill{display:inline-flex;align-items:center;gap:8px;height:42px;padding:0 22px;border-radius:21px;font:700 13px 'Roboto',sans-serif;color:var(--white);text-transform:uppercase;letter-spacing:.2px}
.pill.green{background:var(--green)}
.pill.blue{background:var(--blue)}
.pill .dot{width:13px;height:13px;border-radius:50%;background:var(--white);position:relative}
.pill .dot::after{content:"";position:absolute;left:4px;top:3px;border-left:5px solid currentColor;border-top:3.5px solid transparent;border-bottom:3.5px solid transparent}
.pill.green .dot::after{border-left-color:var(--green)}
.pill.blue .dot::after{border-left-color:var(--blue)}
.main-nav{position:absolute;top:76px;right:112px;display:flex;gap:31px;font:500 14.5px 'Roboto',sans-serif;color:var(--ink);text-transform:uppercase}
.main-nav .active{color:var(--green);position:relative}
.main-nav .active::after{content:"";position:absolute;left:0;right:0;bottom:-7px;height:3px;background:var(--green);border-radius:2px}

/* hero */
.hero{position:absolute;left:0;top:111px;width:1200px;height:664px;overflow:hidden}
.hero-photo{position:absolute;inset:0;background:linear-gradient(110deg,#c9b59c 0%,#8d7258 30%,#5f6a49 45%,#d9d2c6 70%,#eeeae4 100%)}
.hero-wave{position:absolute;left:0;bottom:0;width:1200px;height:200px}
.wand-handle{position:absolute;left:788px;top:430px;width:32px;height:140px;border-radius:16px;background:var(--green);transform:rotate(32deg);transform-origin:top center}
.hero-card{position:absolute;left:694px;top:101px;width:392px;height:392px;border-radius:50%;background:var(--white);border:6px solid var(--blue);text-align:center;padding-top:70px}
.hero-card .rule{width:76px;height:3px;background:var(--green);margin:0 auto 14px}
.hero-card h1{font-family:'Montserrat',sans-serif;font-size:37px;line-height:46px;font-weight:700;color:var(--blue)}
.hero-card h1 span{display:block;font-weight:300;color:var(--green)}
.hero-card p{font-size:18px;line-height:27px;color:var(--ink);margin:14px 28px 0}
.hero-card .pill{margin-top:26px;height:46px;background:var(--green)}
.slider-dots{position:absolute;left:1136px;top:270px;display:flex;flex-direction:column;align-items:center;gap:14px}
.slider-dots i{display:block;width:7px;height:7px;border-radius:50%;background:var(--blue)}
.slider-dots i.on{width:22px;height:22px;background:var(--green);border:6px solid var(--green-soft)}
.hero-badge{position:absolute;left:563px;top:556px;width:72px;height:72px;border-radius:50%;background:var(--white);border:3px solid #e6ebf2;display:flex;align-items:center;justify-content:center}
.hero-badge b{width:36px;height:36px;border-radius:50%;border:2px solid var(--blue)}

/* feature sections */
.band{position:absolute;left:0;width:1200px}
.band.blue{background:var(--blue)}
.band.green{background:var(--green)}
.band.grey{background:var(--grey-band)}
.photo{position:absolute;width:442px;height:442px;border-radius:50%}
.ring{position:absolute;width:442px;height:442px;border-radius:50%}
.badge{position:absolute;width:120px;height:120px;border-radius:50%;background:var(--white);box-shadow:0 6px 20px rgba(0,0,0,.12);display:flex;align-items:center;justify-content:center}
.copy{position:absolute;width:460px}
.copy .rule{width:76px;height:3px;background:var(--green);margin-bottom:14px}
.copy h2{font-family:'Montserrat',sans-serif;font-size:38px;line-height:46px;font-weight:700;color:var(--blue)}
.copy h2 span{display:block;font-weight:300;color:var(--green)}
.copy p{font-size:15px;line-height:26px;margin-top:20px}
.copy ul{list-style:none;margin-top:18px}
.copy li{position:relative;padding-left:37px;font-size:15px;line-height:26px;margin-bottom:9px}
.copy li::before{content:"";position:absolute;left:0;top:6px;width:14px;height:14px;border-radius:50%;border:2px solid var(--blue);box-sizing:border-box}
.copy li::after{content:"";position:absolute;left:5px;top:11px;width:4px;height:4px;border-radius:50%;background:var(--blue)}
.copy .pill{margin-top:20px;height:46px;padding:0 24px}
.copy.on-dark .rule{background:var(--white)}
.copy.on-dark h2,.copy.on-dark h2 span,.copy.on-dark li{color:var(--white)}
.copy.on-dark li::before{border-color:var(--white)}
.copy.on-dark li::after{background:var(--white)}
.copy li a{color:var(--white)}

/* compare quotes */
.compare-title{position:absolute;left:0;width:1200px;top:3718px;text-align:center;font-family:'Montserrat',sans-serif;font-size:37px;font-weight:700;color:var(--blue)}
.compare-title span{font-weight:300;color:var(--green)}
.compare-rule{position:absolute;left:562px;top:3707px;width:76px;height:3px;background:var(--green)}
.carrier{position:absolute;top:3804px;width:184px;height:90px;background:var(--white);border-radius:8px;box-shadow:0 4px 14px rgba(0,0,0,.08);display:flex;align-items:center;justify-content:center;font:700 19px 'Montserrat',sans-serif;color:#3a3c40}
.carrier.selected{border-bottom:4px solid var(--green)}
.arrow{position:absolute;top:3830px;width:38px;height:38px;border-radius:50%;display:flex;align-items:center;justify-content:center}
.arrow.prev{left:37px;border:2px solid var(--green);background:var(--white)}
.arrow.next{left:1126px;background:var(--green)}

/* footer */
.footer-wave{position:absolute;left:0;top:3990px;width:1200px;height:120px}
.site-footer{position:absolute;left:0;top:4108px;width:1200px;height:278px;background:var(--footer);color:#d9dbe0}
.f-col{position:absolute;top:30px}
.f-col h4{font:500 15px 'Roboto',sans-serif;color:var(--white);text-transform:uppercase;margin-bottom:18px}
.f-col li{list-style:none;position:relative;padding-left:33px;font-size:13.5px;line-height:21px;margin-bottom:11px}
.f-col li::before{content:"";position:absolute;left:0;top:4px;width:13px;height:13px;border-radius:50%;background:var(--green)}
.f-col li::after{content:"";position:absolute;left:5px;top:7.5px;border-left:4px solid var(--footer);border-top:3px solid transparent;border-bottom:3px solid transparent}
.f-col.contact li::before,.f-col.contact li::after{display:none}
.f-col.contact svg{position:absolute;left:0;top:3px}
.f-brand{position:absolute;left:854px;top:74px;font-family:'Montserrat',sans-serif;font-size:38px;color:var(--white);letter-spacing:-.5px}
.socials{position:absolute;left:893px;top:160px;display:flex;gap:8px}
.socials i{width:34px;height:34px;border-radius:50%;background:var(--white)}
.socials i:first-child{background:var(--green)}
.footer-line{position:absolute;left:111px;right:111px;top:232px;height:1px;background:#4a4d53}
.copyright{position:absolute;left:0;width:1200px;top:245px;text-align:center;font-size:12px;color:#d9dbe0}
</style>
</head>
<body>

<header class="site-header">
  <div class="brand">CoverLantern</div>
  <div class="top-actions">
    <span class="pill green"><span class="dot"></span>Continue Application</span>
    <span class="pill blue"><span class="dot"></span>Client Login</span>
  </div>
  <nav class="main-nav">
    <span class="active">Home</span><span>Free Quote</span><span>No Exam</span><span>Articles</span><span>FAQ's</span><span>About</span><span>Contact</span>
  </nav>
</header>

<section class="hero">
  <div class="hero-photo" role="img" aria-label="Photo of a grown daughter hugging her smiling mother at a laptop in a warm home kitchen"></div>
  <div class="wand-handle"></div>
  <div class="hero-card">
    <div class="rule"></div>
    <h1>TERM LIFE<span>INSURANCE</span></h1>
    <p>Purchase Life Insurance Online | Quote Yourself | Apply in minutes</p>
    <span class="pill"><span class="dot"></span>Get a Quote</span>
  </div>
  <div class="slider-dots"><i></i><i class="on"></i><i></i><i></i></div>
  <svg class="hero-wave" viewBox="0 0 1200 200" preserveAspectRatio="none">
    <path d="M0 160 C180 95 380 50 600 52 L600 78 C400 78 200 125 0 200 Z" fill="var(--green)"/>
    <path d="M600 66 C850 76 1010 108 1200 0 L1200 40 C1020 135 850 92 600 84 Z" fill="var(--blue)"/>
    <path d="M0 200 C200 128 400 76 600 78 C850 84 1010 128 1200 36 L1200 200 Z" fill="#ffffff"/>
  </svg>
  <div class="hero-badge"><b></b></div>
</section>

<!-- Life insurance online -->
<div class="photo" style="left:113px;top:771px;background:radial-gradient(circle at 40% 40%,#c9c3bb,#8a8f97 55%,#4f5a68)" role="img" aria-label="Photo of a senior couple reviewing a policy with an advisor at a laptop"></div>
<div class="badge" style="left:437px;top:1092px">
  <svg width="58" height="58" viewBox="0 0 58 58" fill="none" stroke="var(--blue)" stroke-width="2.5"><path d="M29 46 C14 36 8 28 8 20 a10 10 0 0 1 21 -3 a10 10 0 0 1 21 3 c0 8 -6 16 -21 26Z"/><path d="M29 22v12M23 28h12" stroke="var(--green)"/></svg>
</div>
<div class="copy" style="left:633px;top:868px">
  <div class="rule"></div>
  <h2>LIFE INSURANCE<span>ONLINE</span></h2>
  <p>Compare quotes from America's top insurance carriers Pick your policy and apply in minutes</p>
  <span class="pill green"><span class="dot"></span>Get Your Quote</span>
</div>

<!-- Compare and save -->
<section class="band blue" style="top:1294px;height:575px"></section>
<div class="ring" style="left:657px;top:1360px;background:var(--green)"></div>
<div class="photo" style="left:643px;top:1360px;background:radial-gradient(circle at 45% 40%,#e9e5df,#b4aea6 55%,#5b636f)" role="img" aria-label="Photo of a couple smiling while reviewing quotes on a tablet"></div>
<div class="badge" style="left:643px;top:1686px">
  <svg width="58" height="58" viewBox="0 0 58 58" fill="none" stroke="var(--green)" stroke-width="2.5"><path d="M12 6h24l8 8v36H12Z"/><path d="M18 20h18M18 27h18M18 34h10"/><path d="M40 30l9 4v7c0 5-4 8-9 10-5-2-9-5-9-10v-7Z" stroke="var(--blue)"/></svg>
</div>
<div class="copy on-dark" style="left:111px;top:1405px">
  <div class="rule"></div>
  <h2>COMPARE AND<span>SAVE</span></h2>
  <ul>
    <li>Get Quotes without having to enter your contact information.</li>
    <li>Decide what's best for you without having to deal with pushy insurance agents.</li>
    <li>Virtual agent tools are available to help you choose what life insurance policy is best for you and your family.</li>
  </ul>
  <span class="pill green"><span class="dot"></span>Compare Carriers</span>
</div>

<!-- Virtual agent -->
<div class="photo" style="left:113px;top:1946px;background:radial-gradient(circle at 40% 40%,#efe7de,#c3a995 50%,#6b5f58)" role="img" aria-label="Photo of a young couple meeting an agent across a table"></div>
<div class="badge" style="left:437px;top:2268px">
  <svg width="58" height="58" viewBox="0 0 58 58" fill="none" stroke="var(--green)" stroke-width="2.5"><rect x="8" y="10" width="30" height="20" rx="6"/><path d="M16 30l-3 7 9-7"/><rect x="22" y="24" width="28" height="18" rx="6" stroke="var(--blue)"/><path d="M28 33h16" stroke="var(--blue)"/></svg>
</div>
<div class="copy" style="left:633px;top:1978px">
  <div class="rule"></div>
  <h2>VIRTUAL<span>AGENT</span></h2>
  <ul>
    <li>Our Virtual Agent Lumi can help you calculate how much death benefit you need.</li>
    <li>Lumi can help you figure out what type of Life Insurance is right for you and your family.</li>
    <li>Lumi can evaluate your health history and provide you with accurate quotes.</li>
  </ul>
  <span class="pill green"><span class="dot"></span>Get Your Quote</span>
</div>

<!-- Live agent -->
<section class="band green" style="top:2476px;height:574px"></section>
<div class="ring" style="left:657px;top:2541px;background:var(--blue)"></div>
<div class="photo" style="left:643px;top:2541px;background:radial-gradient(circle at 55% 40%,#eef1f4,#b7c1cc 55%,#55606d)" role="img" aria-label="Photo of a support agent wearing a headset in a bright call centre"></div>
<div class="badge" style="left:643px;top:2866px">
  <svg width="58" height="58" viewBox="0 0 58 58" fill="none" stroke="var(--blue)" stroke-width="2.5"><circle cx="30" cy="20" r="8"/><circle cx="30" cy="20" r="14" stroke-dasharray="5 4"/><path d="M6 44h10l8 4h14l12-8-4-3-10 5h-9" stroke="var(--green)"/></svg>
</div>
<div class="copy on-dark" style="left:111px;top:2575px">
  <div class="rule"></div>
  <h2>LIVE AGENT<span>SUPPORT</span></h2>
  <ul>
    <li>If you need a Live Agent, CoverLantern has you covered. CoverLantern Agents are not paid a commission. So if you have questions our agents have the answers that best suit your needs.</li>
    <li>Call Toll Free: <b>1-888-555-0142</b></li>
    <li>Email: <a href="#"><b>info@CoverLantern.com</b></a></li>
  </ul>
  <span class="pill blue"><span class="dot"></span>Get Your Quote</span>
</div>

<!-- Apply online -->
<div class="photo" style="left:113px;top:3125px;background:radial-gradient(circle at 45% 40%,#f1ece6,#c9b7a5 55%,#6d655e)" role="img" aria-label="Photo of a couple reviewing papers together beside a laptop"></div>
<div class="badge" style="left:437px;top:3449px">
  <svg width="58" height="58" viewBox="0 0 58 58" fill="none" stroke="var(--blue)" stroke-width="2.5"><rect x="14" y="8" width="30" height="34" rx="3"/><circle cx="29" cy="20" r="5"/><path d="M21 34c2-5 14-5 16 0"/><path d="M6 46h46v4H6Z" stroke="var(--green)"/></svg>
</div>
<div class="copy" style="left:633px;top:3186px">
  <div class="rule"></div>
  <h2>APPLY<span>ONLINE</span></h2>
  <ul>
    <li>Pick your policy and apply online in minutes.</li>
    <li>Secure Online Portal keeps your information safe and secure.</li>
    <li>24/7 access to your policy documents.</li>
  </ul>
  <span class="pill green"><span class="dot"></span>Portal Login</span>
</div>

<!-- Compare quotes -->
<section class="band grey" style="top:3659px;height:450px"></section>
<div class="compare-rule"></div>
<h2 class="compare-title">COMPARE <span>QUOTES</span></h2>
<div class="arrow prev"><svg width="12" height="12" viewBox="0 0 12 12"><path d="M8 2L4 6l4 4" fill="none" stroke="var(--green)" stroke-width="2"/></svg></div>
<div class="carrier" style="left:111px">Northgate Mutual</div>
<div class="carrier selected" style="left:310px">Prairie Shield</div>
<div class="carrier" style="left:509px">Keystone Life</div>
<div class="carrier" style="left:706px">Bayline</div>
<div class="carrier" style="left:904px">Harlow &amp; Co</div>
<div class="arrow next"><svg width="12" height="12" viewBox="0 0 12 12"><path d="M4 2l4 4-4 4" fill="none" stroke="#fff" stroke-width="2"/></svg></div>
<span class="pill green abs" style="left:521px;top:3941px;height:44px"><span class="dot"></span>Free Quotes</span>

<!-- Footer -->
<svg class="footer-wave" viewBox="0 0 1200 120" preserveAspectRatio="none">
  <path d="M0 70 C250 20 450 30 650 50 C850 70 1000 50 1200 0 L1200 30 C1000 80 850 95 650 80 C450 65 250 60 0 110 Z" fill="var(--green)"/>
  <path d="M0 95 C220 50 430 60 650 80 C850 98 1000 80 1200 30 L1200 120 L0 120 Z" fill="var(--footer)"/>
  <path d="M0 70 C120 45 200 35 300 32 C200 45 100 75 0 110 Z" fill="var(--blue)"/>
</svg>
<footer class="site-footer">
  <div class="f-col" style="left:111px">
    <h4>Life Insurance</h4>
    <ul><li>10 Year Level Team</li><li>15 Year Level Team</li><li>20 Year Level Team</li><li>30 Year Level Team</li><li>Lifetime Coverage</li></ul>
  </div>
  <div class="f-col" style="left:351px">
    <h4>Tools</h4>
    <ul><li>Quote Comparison</li><li>Secure Client Portal</li><li>Privacy Policy</li><li>Contact Us</li></ul>
  </div>
  <div class="f-col contact" style="left:584px;width:230px">
    <h4>Contact</h4>
    <ul>
      <li><svg width="12" height="15" viewBox="0 0 12 15"><path d="M6 0a6 6 0 0 1 6 6c0 4-6 9-6 9S0 10 0 6a6 6 0 0 1 6-6Z" fill="var(--green)"/><circle cx="6" cy="6" r="2" fill="var(--footer)"/></svg>4870 Harbor Lake Road, Suite 110 Clearwater, FL 33760</li>
      <li><svg width="14" height="14" viewBox="0 0 14 14"><path d="M3 0l3 3-2 2c1 2 3 4 5 5l2-2 3 3-2 3C6 14 0 8 0 3Z" fill="var(--green)"/></svg>1-888-555-0142</li>
      <li><svg width="15" height="11" viewBox="0 0 15 11"><rect width="15" height="11" rx="1" fill="var(--green)"/><path d="M0 1l7.5 5L15 1" fill="none" stroke="var(--footer)" stroke-width="1.5"/></svg>info@CoverLantern.com</li>
    </ul>
  </div>
  <div class="f-brand">CoverLantern</div>
  <div class="socials" aria-label="Social links"><i></i><i></i><i></i><i></i></div>
  <div class="footer-line"></div>
  <div class="copyright">© 2022 CoverLantern / All Rights Reserved</div>
</footer>

</body>
</html>
```